vosk hire pricelist

Hi There,

Can we please edit this price list?

The borders need to be lined up and all color coordinated for us.

There are quite a few areas where everything is misjoined and not lining up correctly.

```html
<!DOCTYPE html>
<html lang="en">
<head>
<meta charset="utf-8">
<title>Vosk Hire – Price List</title>
<link href="https://fonts.googleapis.com/css2?family=Oswald:wght@600&family=Roboto:wght@300;400;700&display=swap" rel="stylesheet">
<style>
:root{
  --green:#8dc63f;
  --row:#e5eed6;
  --row-alt:#eef3e6;
  --weekly:#d3d6d0;
  --head-cell:#d9dbd7;
  --ink:#1d1d1b;
  --note:#6b6b6b;
  --stage:#e4e4e4;
  --notice:#ececec;
}
*{box-sizing:border-box;margin:0;padding:0}
html,body{width:1200px;height:853px;overflow:hidden;background:var(--stage);font-family:"Roboto",sans-serif;color:var(--ink)}
.sheet{position:absolute;top:49px;width:505px;height:713px;background:#fff;overflow:hidden}
.sheet--one{left:80px}
.sheet--two{left:634px}
.masthead{position:absolute;left:0;top:0;width:505px;height:152px}
.masthead__photo{position:absolute;left:0;top:0;width:505px;height:140px;background:linear-gradient(180deg,#3d3b3a 0%,#5a534b 55%,#3e4a30 100%)}
.masthead__band{position:absolute;left:0;top:0}
.brand{position:absolute;left:12px;top:48px;font:700 25px/1 "Roboto",sans-serif;color:var(--green);letter-spacing:-0.5px}
.tagline{position:absolute;left:373px;top:28px;font:600 17px/17px "Oswald",sans-serif;color:#fff;text-transform:uppercase}
.tagline .accent{color:var(--green)}
.contact{position:absolute;left:12px;top:137px;font:400 9px/1 "Roboto",sans-serif;color:#fff}
.call{position:absolute;right:14px;top:121px;display:flex;align-items:center;gap:4px;color:#fff}
.call__label{font:400 6px/7px "Roboto",sans-serif;text-align:right}
.call__number{font:300 19px/1 "Roboto",sans-serif;letter-spacing:0.3px}
.notice{position:absolute;left:12px;top:157px;width:481px;height:15px;background:var(--notice);font-size:6.6px;line-height:15px;text-align:center}
.column{position:absolute;top:177px;width:234px}
.column--left{left:12px}
.column--right{left:258px}
.price-table{width:234px;border-collapse:collapse;table-layout:fixed;font-size:6.5px}
.price-table col.name{width:144px}
.price-table col.day,.price-table col.week{width:45px}
.price-table td,.price-table th{height:11px;line-height:10px;padding:0 3px;border-bottom:1px solid #fff;white-space:nowrap;overflow:hidden}
.price-table td{background:var(--row)}
.price-table td:nth-child(2){background:var(--row-alt);text-align:right}
.price-table td:nth-child(3){background:var(--weekly);text-align:right}
.price-table td.span{text-align:left;background:var(--row-alt)}
.price-table td.center{text-align:center}
.price-table th{font-weight:700;text-align:right;background:var(--head-cell)}
.price-table th:first-child{background:var(--green);color:#fff;text-align:left;letter-spacing:0.3px}
.price-table tr.tall th,.price-table tr.tall td{height:18px;white-space:normal;line-height:8px}
.price-table tr.tall th{vertical-align:middle}
.site-photo{position:absolute;left:258px;top:515px;width:234px;height:138px;background:linear-gradient(180deg,#7f8f9e 0%,#a9a27a 45%,#4f6a30 70%,#6b5235 100%)}
.price-note{position:absolute;left:258px;top:659px;width:234px;height:26px;background:var(--note);color:#fff;font-size:7px;line-height:8.5px;padding:4px 7px}
.footer{position:absolute;left:0;top:691px;width:505px;height:22px;background:var(--green);color:#fff;font-size:6.6px;display:flex;align-items:center;justify-content:space-between;padding:0 12px}
.footer__page{position:absolute;left:0;right:0;text-align:center}
</style>
</head>
<body>

<section class="sheet sheet--one">
  <header class="masthead">
    <div class="masthead__photo" role="img" aria-label="Excavator digging at a construction site under a dusky sky"></div>
    <svg class="masthead__band" width="505" height="152" viewBox="0 0 505 152"><path d="M0 134 L290 134 C302 134 306 118 322 118 L505 118 L505 152 L0 152 Z" fill="#8dc63f"/></svg>
    <div class="brand">VOSK HIRE</div>
    <div class="tagline">The<br><span class="accent">Construction</span><br>Industry<br>Specialists</div>
    <div class="contact">hire@voskhire.com.au &nbsp;|&nbsp; www.voskhire.com.au</div>
    <div class="call">
      <span class="call__label">CALL US<br>NOW</span>
      <svg width="22" height="22" viewBox="0 0 24 24" fill="none" stroke="#fff" stroke-width="1.6"><path d="M6.6 3.5 9 7.8 7.3 9.6c1 2.6 3.3 4.9 6 6l1.8-1.7 4.4 2.3-.9 3.6c-.3.8-1 1.2-1.9 1.1C9.8 19.9 4 14.2 3.3 7.3c-.1-.9.4-1.6 1.1-1.9z"/><path d="M14 4a7 7 0 0 1 6 6M14 7.5a3.5 3.5 0 0 1 2.6 2.6"/></svg>
      <span class="call__number">(03) 9000 4127</span>
    </div>
  </header>

  <p class="notice">Mobile scaffold towers $50 per vertical metre - per week - $80 delivery e/w - erection by licensed scaffolders available. Melbourne Metro ute deliveries $50*</p>

  <div class="column column--left">
    <table class="price-table">
      <colgroup><col class="name"><col class="day"><col class="week"></colgroup>
      <tr><th>LADDERS AND TRESTLES</th><th>DAILY</th><th>WEEKLY</th></tr>
      <tr><td>Steel Props #0-#4 (Min 1 Week)</td><td>$14.50</td><td>$14.50</td></tr>
      <tr><td>Extension Ladder 15/21 Ft</td><td>$30.00</td><td>$60.00</td></tr>
      <tr><td>Extension Ladder 15/21 Ft</td><td>$30.00</td><td>$60.00</td></tr>
      <tr><td>Step Ladder 6ft - 8 ft</td><td>$30.00</td><td>$60.00</td></tr>
      <tr><td>Step Ladder 10ft - 12 ft</td><td>$30.00</td><td>$60.00</td></tr>
      <tr><td>Trestles (Each) 6ft - 12 ft</td><td>$30.00</td><td>$60.00</td></tr>
      <tr><td>Planks 4m, 5m, 6m (Aluminium)</td><td>$18.00</td><td>$35.00</td></tr>
      <tr><td>Aluminium Scaffold Towers</td><td class="span" colspan="2">$50 vertical metre</td></tr>
      <tr><th>AIR/HYDRAULIC TOOLS</th><th>DAILY</th><th>WEEKLY</th></tr>
      <tr><td>Compressor (17 CFM Electric)</td><td>$66.00</td><td>$225.00</td></tr>
      <tr><td>Compressor Hose and NailGun</td><td>$66.00</td><td>$225.00</td></tr>
      <tr><td>Coil Nail Gun</td><td>$66.00</td><td>$225.00</td></tr>
      <tr><td>Nail Gun – Framing</td><td>$66.00</td><td>$225.00</td></tr>
      <tr><td>Nail Gun – Gas</td><td>$66.00</td><td>$225.00</td></tr>
      <tr><td>Secret Nail Gun</td><td>$66.00</td><td>$225.00</td></tr>
      <tr><td>Staple Gun</td><td>$66.00</td><td>$225.00</td></tr>
      <tr><th>PLASTER CEILING AND ROOF TOOLS</th><th>DAILY</th><th>WEEKLY</th></tr>
      <tr><td>Panel Lift</td><td>$66.00</td><td>$210.00</td></tr>
      <tr><th>LASER LEVELS AND MEASURING TOOLS</th><th>DAILY</th><th>WEEKLY</th></tr>
      <tr><td>Laser Level Tripod and Staff</td><td>$99.00</td><td>$380.00</td></tr>
      <tr><td>Tape Measure 60m</td><td>$15.84</td><td>$15.84</td></tr>
      <tr><th>TARPAULINS</th><th>DAILY</th><th>WEEKLY</th></tr>
      <tr><td>Tarpaulins 6m x 9m</td><td></td><td>$84.00</td></tr>
      <tr><th>TEMPORARY FENCING</th><th>DAILY</th><th>WEEKLY</th></tr>
      <tr><td>Temporary Fencing - per metre per month</td><td></td><td>4.2 p/m</td></tr>
      <tr><th>TOILETS</th><th>DAILY</th><th>WEEKLY</th></tr>
      <tr><td>Portable Toilet</td><td></td><td>$45.00</td></tr>
      <tr><td>Toilet Pump-outs - SS</td><td></td><td></td></tr>
      <tr><td>Sewer Connected Toilet</td><td></td><td>$45.00</td></tr>
      <tr><td>Toilet on Trailer</td><td>$120.00</td><td>$300.00</td></tr>
      <tr><th>CLEANING EQUIPMENT AND PUMP</th><th>DAILY</th><th>WEEKLY</th></tr>
      <tr><td>Flex Drive Pump</td><td>$66.00</td><td>$145.00</td></tr>
      <tr><td>Flex Drive Motor</td><td>$66.00</td><td>$145.00</td></tr>
      <tr><td>Sub Pump 2 - Float or Non Float</td><td>$79.20</td><td>$185.00</td></tr>
      <tr><th>VACUUM CLEANERS</th><th>DAILY</th><th>WEEKLY</th></tr>
      <tr><td>Vacuum Cleaner 2 Motor Industrial Wet &amp; Dry</td><td>$86.00</td><td>$290.00</td></tr>
      <tr><td>Vacuum Cleaner - Plaster Dust</td><td>$105.00</td><td>$572.00</td></tr>
      <tr><th>PRESSURE CLEANERS</th><th>DAILY</th><th>WEEKLY</th></tr>
      <tr><td>Electric Pressure Washer 2000 PSI</td><td>$125.40</td><td>$290.00</td></tr>
      <tr><td>Petrol Pressure Washer 4000 PSI</td><td>$158.40</td><td>$572.00</td></tr>
      <tr><th>COMPACTING EQUIPMENT</th><th>DAILY</th><th>WEEKLY</th></tr>
      <tr><td>Vibrating Plate Small/ Standard</td><td>$71.50</td><td>$264.00</td></tr>
      <tr><td>VPC 3.7t Compactor</td><td>$141.90</td><td>$638.00</td></tr>
      <tr><td>VPC 6t Compactor</td><td>$141.90</td><td>$638.00</td></tr>
      <tr><td>Vardel Rammer</td><td>$144.00</td><td>$396.00</td></tr>
    </table>
  </div>

  <div class="column column--right">
    <table class="price-table">
      <colgroup><col class="name"><col class="day"><col class="week"></colgroup>
      <tr><th>CONCRETE EQUIPMENT</th><th>DAILY</th><th>WEEKLY</th></tr>
      <tr><td>Concrete Screed 2m / 3m</td><td>$18.00</td><td>$52.00</td></tr>
      <tr><td>Troweling Machine (Petrol)</td><td>$93.50</td><td>$374.00</td></tr>
      <tr><th>GRINDERS, PLANERS AND MOWERS</th><th>DAILY</th><th>WEEKLY</th></tr>
      <tr><td>Concrete Floor Grinder (Diamonds Extra)</td><td>$105.60</td><td>$364.00</td></tr>
      <tr><td>9 Inch Grinder with Diamond Disc</td><td>$88.00</td><td>$320.00</td></tr>
      <tr><td>Concrete Dust Vacuum Cleaner</td><td>$105.60</td><td>$340.00</td></tr>
      <tr><th>CONCRETE/ BRICK SAWS AND CUTTERS</th><th>DAILY</th><th>WEEKLY</th></tr>
      <tr><td>Demo Saw 14”</td><td>$158.00</td><td>$550.00</td></tr>
      <tr><td>Demo Saw 16”</td><td>$158.00</td><td>$550.00</td></tr>
      <tr><td>Pedestrian Concrete Saw 18”</td><td>$198.00</td><td>$607.00</td></tr>
      <tr><th>AIR TOOLS HEAVY DUTY</th><th>DAILY</th><th>WEEKLY</th></tr>
      <tr><td>Compressor (130 CFM Diesel)</td><td>$171.00</td><td>$550.00</td></tr>
      <tr><td>Beam Blower</td><td>$13.00</td><td>$40.00</td></tr>
      <tr><td>Breaker Heavy</td><td>$66.00</td><td>$132.00</td></tr>
      <tr><th>BRICK/CONCRETE, TIMBER &amp; TILE TOOLS</th><th>DAILY</th><th>WEEKLY</th></tr>
      <tr><td>Brick Saw / Paver Inc. Diamond Blade</td><td>$145.00</td><td>$420.00</td></tr>
      <tr><td>Demo Saw 16” (Blade included)</td><td>$158.00</td><td>$550.00</td></tr>
      <tr><td>Pedestrian Concrete Saw</td><td>$198.00</td><td>$528.00</td></tr>
      <tr><td>Wall Chaser</td><td>$141.00</td><td>$450.00</td></tr>
      <tr><td>Grinder 225mm (Diamond Blade)</td><td>$105.00</td><td>$290.00</td></tr>
      <tr><td>Timbrecut Saw (Brick &amp; Mortar Saw)</td><td>$120.00</td><td>$420.00</td></tr>
      <tr><td>Sabre Saw</td><td>$46.00</td><td>$165.00</td></tr>
      <tr><td>Saw Circular 235mm</td><td>$52.80</td><td>$145.00</td></tr>
      <tr><td>Core Hole Drill - (Diamonds Extra)</td><td>$200.00</td><td>$600.00</td></tr>
      <tr><td>Jamb Saw</td><td>$140.00</td><td>$480.00</td></tr>
      <tr><td>Tile Saw 900 mm</td><td>$145.00</td><td>$420.00</td></tr>
      <tr><td>Lock Mortiser</td><td>$191.00</td><td>$540.00</td></tr>
      <tr><td>Wood Router</td><td>$46.00</td><td>$165.00</td></tr>
      <tr><th>DRILLS</th><th>DAILY</th><th>WEEKLY</th></tr>
      <tr><td>Cordless Hand Drill / Driver</td><td>$39.60</td><td>$184.00</td></tr>
      <tr><td>Drill Magnetic</td><td>$132.00</td><td>$462.00</td></tr>
      <tr><td>Plaster Screw Gun</td><td>$55.00</td><td>$180.00</td></tr>
      <tr><td>Fastening Gun</td><td>$60.00</td><td>$198.00</td></tr>
      <tr><td>Drill Bits (All Makes)</td><td>$13.00</td><td>$53.00</td></tr>
      <tr><td>Impact Hammer Drill</td><td>$72.00</td><td>$264.00</td></tr>
      <tr><td>Hammer Drill Bits</td><td>$12.00</td><td>$38.00</td></tr>
      <tr><th>JACKHAMMERS</th><th>DAILY</th><th>WEEKLY</th></tr>
      <tr><td>Jackhammer Small Electric</td><td>$65.00</td><td>$255.00</td></tr>
      <tr><td>Jackhammer Medium</td><td>$71.00</td><td>$286.00</td></tr>
      <tr><td>Jackhammer Large</td><td>$112.00</td><td>$440.00</td></tr>
      <tr><td>Tile Remover Attachment</td><td>$39.00</td><td>$158.00</td></tr>
      <tr><td>Spade Tool (All Makes)</td><td>$13.00</td><td>$48.00</td></tr>
      <tr><th>SAFETY EQUIPMENT</th><th>DAILY</th><th>WEEKLY</th></tr>
      <tr><td>Roof Safety Harness Kit</td><td>$24.00</td><td>$84.00</td></tr>
      <tr><td></td><td></td><td></td></tr>
      <tr><td></td><td></td><td></td></tr>
      <tr><td></td><td></td><td></td></tr>
    </table>
  </div>

  <footer class="footer">
    <span>©VOSKHIRE 2022</span>
    <span class="footer__page">PAGE <b>1</b> OF 2</span>
    <span>Expertise to provide total hire solutions</span>
  </footer>
</section>

<section class="sheet sheet--two">
  <header class="masthead">
    <div class="masthead__photo" role="img" aria-label="Excavator digging at a construction site under a dusky sky"></div>
    <svg class="masthead__band" width="505" height="152" viewBox="0 0 505 152"><path d="M0 134 L290 134 C302 134 306 118 322 118 L505 118 L505 152 L0 152 Z" fill="#8dc63f"/></svg>
    <div class="brand">VOSK HIRE</div>
    <div class="tagline">The<br><span class="accent">Construction</span><br>Industry<br>Specialists</div>
    <div class="contact">hire@voskhire.com.au &nbsp;|&nbsp; www.voskhire.com.au</div>
    <div class="call">
      <span class="call__label">CALL US<br>NOW</span>
      <svg width="22" height="22" viewBox="0 0 24 24" fill="none" stroke="#fff" stroke-width="1.6"><path d="M6.6 3.5 9 7.8 7.3 9.6c1 2.6 3.3 4.9 6 6l1.8-1.7 4.4 2.3-.9 3.6c-.3.8-1 1.2-1.9 1.1C9.8 19.9 4 14.2 3.3 7.3c-.1-.9.4-1.6 1.1-1.9z"/><path d="M14 4a7 7 0 0 1 6 6M14 7.5a3.5 3.5 0 0 1 2.6 2.6"/></svg>
      <span class="call__number">(03) 9000 4127</span>
    </div>
  </header>

  <p class="notice">Mobile scaffold towers $50 per vertical metre - per week - $80 delivery e/w - erection by licensed scaffolders available.</p>

  <div class="column column--left">
    <table class="price-table">
      <colgroup><col class="name"><col class="day"><col class="week"></colgroup>
      <tr class="tall"><th>EARTHMOVING, MINI LOADERS, ATTACHMENTS</th><th>DAILY</th><th>WEEKLY</th></tr>
      <tr><td>Mini Loader - Kimba - Large or Small</td><td>$300.00</td><td>$1,000.00</td></tr>
      <tr><td>Vardel Tracked Dumper</td><td>$180.00</td><td>$700.00</td></tr>
      <tr><td>Mini Loader c/w Post Hole Digger</td><td>$336.00</td><td>$1,280.00</td></tr>
      <tr><td>Mini Loader c/w Trencher</td><td>$372.00</td><td>$1,152.00</td></tr>
      <tr><th>EXCAVATORS</th><th>DAILY</th><th>WEEKLY</th></tr>
      <tr><td>Mini Excavator - 1 Tonne - Min 740 Wide</td><td>$240.00</td><td>$1,100.00</td></tr>
      <tr><td>Mini Excavator - 1.7 Tonne - 980 Wide</td><td>$240.00</td><td>$1,100.00</td></tr>
      <tr><td>Excavator - 3.5 Tonne - Trans $180</td><td>$320.00</td><td>$1,300.00</td></tr>
      <tr><td>Excavator - 5 Tonne - Trans $240</td><td>$420.00</td><td>$1,600.00</td></tr>
      <tr><td>Excavator - 8 Tonne - Trans $300</td><td>$460.00</td><td>$1,800.00</td></tr>
      <tr><td>Excavators up to 22 Tonne</td><td class="center">P.O.A</td><td></td></tr>
      <tr><td>1.7T Breaker - ST Breaker</td><td></td><td>$500.00</td></tr>
      <tr><td>3.5T Breaker - BT Breaker</td><td></td><td>$650.00</td></tr>
      <tr><td>Augers Ranging from 250mm to 600mm</td><td>$160.00</td><td>$450.00</td></tr>
      <tr><th>MATERIALS HANDLING</th><th>DAILY</th><th>WEEKLY</th></tr>
      <tr><td>Glass Sucker (per pair)</td><td>$24.00</td><td>$39.60</td></tr>
      <tr><td>Piano Trolley</td><td>$29.00</td><td>$79.20</td></tr>
      <tr><td>Hand Trolley</td><td>$23.76</td><td>$66.00</td></tr>
      <tr><td>Pallet Truck (2000 kg)</td><td>$39.60</td><td>$118.80</td></tr>
      <tr><td>Brick/ Block Elevator 6m</td><td>$125.40</td><td>$396.00</td></tr>
      <tr><td>Brick/ Block Elevator 9m</td><td>$145.00</td><td>$480.00</td></tr>
      <tr><td>Chain Block Halmar / 1 Ton/ 2 Ton</td><td>$39.60</td><td>$132.00</td></tr>
      <tr><td>Forklift Gas Operated 2.5 Ton</td><td>$150.00</td><td>$350.00</td></tr>
      <tr><td>Forklift Diesel 2.5T RT Buggy</td><td>$220.00</td><td>$800.00</td></tr>
      <tr><td>Concrete Kibble 1m</td><td>$150.00</td><td>$350.00</td></tr>
      <tr><td>Concrete Kibble 1.5m</td><td>$150.00</td><td>$350.00</td></tr>
      <tr><td>Concrete Kibble Truck</td><td>$50.00</td><td>$150.00</td></tr>
      <tr><td>Brick &amp; Block Cage</td><td>$110.00</td><td>$290.00</td></tr>
      <tr><td>Gas Cage</td><td></td><td>$80.00</td></tr>
      <tr><td>Bin Lifter</td><td>$110.00</td><td>$250.00</td></tr>
      <tr><th>SKID STEERS</th><th>DAILY</th><th>WEEKLY</th></tr>
      <tr><td>Skid Steer 1.2m Wide 5 SDKS</td><td>$312.00</td><td>$1,008.00</td></tr>
      <tr><td>Trakon RT-50 Crawler Loader</td><td>$400.00</td><td>$1,600.00</td></tr>
      <tr><th>LIGHTS</th><th>DAILY</th><th>WEEKLY</th></tr>
      <tr><td>Floodlight 500W Twin on Stand</td><td>$23.76</td><td>$47.52</td></tr>
      <tr><td>Light Tower</td><td>$180.00</td><td>$450.00</td></tr>
      <tr><th>HOISTS AND LIFTERS</th><th>DAILY</th><th>WEEKLY</th></tr>
      <tr><td>Duct Lifter - 250 kg Capacity</td><td>$118.80</td><td>$440.00</td></tr>
      <tr><td>Panel Lift</td><td>$59.40</td><td>$237.60</td></tr>
      <tr><th>TRAFFIC</th><th>DAILY</th><th>WEEKLY</th></tr>
      <tr><td>Traffic Barricade Bollards</td><td>$1.00+</td><td>$6.60</td></tr>
      <tr><td>Barricade Lights</td><td>$10.56</td><td>$39.60</td></tr>
      <tr><td>Roadplates - 2.4m x 1.2m (Transport P.O.A)</td><td></td><td>$110.00</td></tr>
      <tr class="tall"><td>Barrier-Water Filled TL2 Crash Barrier (Per metre)</td><td>$1.75</td><td>$12.25</td></tr>
    </table>
  </div>

  <div class="column column--right">
    <table class="price-table">
      <colgroup><col class="name"><col class="day"><col class="week"></colgroup>
      <tr><th>FANS AND HEATERS</th><th>DAILY</th><th>WEEKLY</th></tr>
      <tr><td>Fan Carpet Dryer</td><td>$59.40</td><td>$184.80</td></tr>
      <tr><td>Fan Carpet Dryer</td><td>$78.00</td><td>$380.00</td></tr>
      <tr><td>Exhaust Fan w/Ducting / 600mm</td><td>$59.40</td><td>$145.20</td></tr>
      <tr><td>Exhaust Fan Ducting $3 per metre</td><td></td><td></td></tr>
      <tr><th>HEATERS</th><th>DAILY</th><th>WEEKLY</th></tr>
      <tr><td>Heater Blower Small / Large (Gas Extra)</td><td>$79.20</td><td>$110.00</td></tr>
      <tr><td>Gas Bottles - Medium - $80 - Large - $160</td><td></td><td></td></tr>
      <tr><th>CONCRETE VIBRATORS</th><th>DAILY</th><th>WEEKLY</th></tr>
      <tr><td>Flex Drive Shaft (Portable)</td><td>$79.20</td><td>$330.00</td></tr>
      <tr><td>Flex Drive Motor (Petrol)</td><td>$66.00</td><td>$145.20</td></tr>
      <tr><td>Flex Drive Shaft - Concrete Vibe</td><td>$39.60</td><td>$132.00</td></tr>
      <tr><th>CONCRETE MIXERS</th><th>DAILY</th><th>WEEKLY</th></tr>
      <tr><td>Mixer Electric</td><td>$132.00</td><td>$158.40</td></tr>
      <tr><th>FLOOR SANDERS</th><th>DAILY</th><th>WEEKLY</th></tr>
      <tr><td>Floor Edger</td><td>$79.20</td><td>$224.40</td></tr>
      <tr><td>Floor Sander 7” Drum - Sand Pads - $8</td><td>$112.20</td><td>$330.00</td></tr>
      <tr><td>Wall Paper Steamer</td><td>$80.00</td><td>$260.00</td></tr>
      <tr><th>GENERATORS</th><th>DAILY</th><th>WEEKLY</th></tr>
      <tr><td>Generator (8 KVA)</td><td>$110.00</td><td>$380.00</td></tr>
      <tr><td>Generator (10 KVA)</td><td>$110.00</td><td>$380.00</td></tr>
      <tr><td>16KVA Generator with 3 Phase</td><td>$200.00</td><td>$450.00</td></tr>
      <tr><td>25KVA Diesel Generator</td><td>$200.00</td><td>$550.00</td></tr>
      <tr><th>LAWN AND TURF CARE</th><th>DAILY</th><th>WEEKLY</th></tr>
      <tr><td>Line Trimmer</td><td>$36.00</td><td>$132.00</td></tr>
      <tr><td>Lawn Mower (4 Stroke)</td><td>$43.56</td><td>$132.00</td></tr>
      <tr><td>Post - Hole Digger One Man/200 mm</td><td>$99.00</td><td>$330.00</td></tr>
      <tr><td>Post - Hole Digger 2-Man</td><td>$118.80</td><td>$448.80</td></tr>
      <tr><td>Leaf Blower (2 Stroke)</td><td>$39.60</td><td>$132.00</td></tr>
      <tr><td>Rotary Hoe</td><td>$130.00</td><td>$450.00</td></tr>
    </table>
  </div>

  <div class="site-photo" role="img" aria-label="Compact excavator digging soil on a grassy site with trees behind"></div>
  <p class="price-note">*Prices effective 01/02/2022 and are subject to change without notice. All prices are exclusive of GST</p>

  <footer class="footer">
    <span>©VOSKHIRE 2022</span>
    <span class="footer__page">PAGE <b>2</b> OF 2</span>
    <span>Expertise to provide total hire solutions</span>
  </footer>
</section>

</body>
</html>
```